DOVR Business Card Design Project

Company Name: DOVR (Dove Operational Versatile Resources) JLT.
Office Address: Office No 218, Saffron Crest Tower, Palmera Bay Towers, Dubai, U.A.E
Company line of business:
1) Currently we have a POS solution for retail outlets like duty free shops, supermarkets, department stores etc... The solution is deployed in Harbor Gate Retail on 350 POS and in Coralline Port Retail on 100 POS. So our main line of business is the deployment of this solution in retail outlets locally or regionally. We have already deployed the solution in India and Australia.
2) Integration of other third party POS systems with an online credit authorization netwotk in the UAE. This will enable POS applications to connect directly to the acquiring banks without needing an EFT terminal like Paxoline or Tramodex. The credit card payment is completed at the POS.
3) Other solutions that are targeting retail outlets like mobile POS, queue busting solutions, stock taking solutions using hand held devices, transaction capture systems, etc...
4) Other IT services like support of call center solutions from Bramwell Systems and development of new solutions as per customer requirements.
We need a business card design for the company. We don't have any specific requirements and will eave up to the designers to come up with creative designs. At the moment we still don't have a letter head design and the only thing that we have is the company logo that we will upload shortly.
Updates
Dear All,
I just uploaded the logo source files. I am sorry for the delay.
Regards
Tarek Demirci
I would like the business cards to have the following details:
Company Tel No
Company Fax No
Company Website Address
Employee Name
Employee Title
Employee Mobile Number
Employee Email Address

```html
<!DOCTYPE html>
<html lang="en">
<head>
<meta charset="utf-8">
<title>DOVR Business Card</title>
<link rel="stylesheet" href="https://fonts.googleapis.com/css2?family=PT+Sans+Narrow:wght@400;700&display=swap">
<style>
  :root {
    --page: #e9e7e3;
    --card: #ffffff;
    --ink-blue: #1a72c2;
    --ink-dark: #2b2b2b;
    --mark-blue: #1a72c2;
    --card-shadow: rgba(0, 0, 0, 0.14);
  }
  * { box-sizing: border-box; margin: 0; padding: 0; }
  html, body {
    width: 1200px;
    height: 820px;
    overflow: hidden;
    background: var(--page);
    font-family: "PT Sans Narrow", "Arial Narrow", sans-serif;
  }
  .canvas {
    position: relative;
    width: 1200px;
    height: 820px;
  }
  .card {
    position: absolute;
    left: 300px;
    width: 600px;
    height: 343px;
    background: var(--card);
    box-shadow: 0 6px 18px var(--card-shadow);
  }
  .card--front { top: 60px; }
  .card--back { top: 433px; }

  /* Front: brand name */
  .brand {
    position: absolute;
    left: 150px;
    top: 118px;
    display: flex;
    align-items: center;
    gap: 18px;
  }
  .brand__dot {
    width: 46px;
    height: 46px;
    border-radius: 50%;
    background: var(--mark-blue);
  }
  .brand__name {
    font-size: 78px;
    font-weight: 400;
    letter-spacing: 6px;
    line-height: 1;
    color: var(--ink-dark);
  }

  /* Back: contact side */
  .person {
    position: absolute;
    right: 392px;
    top: 162px;
    text-align: right;
    color: var(--ink-blue);
  }
  .person__name {
    font-size: 19px;
    font-weight: 700;
    line-height: 1.1;
  }
  .person__title {
    font-size: 16px;
    font-weight: 400;
    line-height: 1.2;
  }
  .contact {
    position: absolute;
    left: 238px;
    top: 56px;
    color: var(--ink-blue);
    font-size: 16px;
    line-height: 20px;
    font-style: normal;
  }
  .contact__address { margin-bottom: 22px; }
  .contact__line { display: block; white-space: nowrap; }
</style>
</head>
<body>
<main class="canvas">
  <section class="card card--front" aria-label="Business card front">
    <div class="brand">
      <span class="brand__dot" aria-hidden="true"></span>
      <span class="brand__name">DOVR</span>
    </div>
  </section>

  <section class="card card--back" aria-label="Business card back">
    <div class="person">
      <p class="person__name">Samir K. Haddad</p>
      <p class="person__title">Founder</p>
    </div>
    <address class="contact">
      <div class="contact__address">
        <span class="contact__line">Office No 218</span>
        <span class="contact__line">Saffron Crest Tower</span>
        <span class="contact__line">Palmera Bay Towers</span>
        <span class="contact__line">Dubai, U.A.E</span>
      </div>
      <div class="contact__details">
        <span class="contact__line">Telephone: +971 4 555 0182</span>
        <span class="contact__line">Fax: +971 4 555 0183</span>
        <span class="contact__line">Mobile: +971 50 555 0147</span>
        <span class="contact__line">email: shaddad@dovr.com</span>
        <span class="contact__line">website: www.dovr.com</span>
      </div>
    </address>
  </section>
</main>
</body>
</html>
```